Steadfast MD - Sleep Medicine Specialist - Business Cards

We are a new medical practice called Steadfast MD. We are sleep medicine specialists and we will be conducting sleep studies on patients with sleep related ailments. We want the business card to be bold, professional, and clean with the logo as the stand out visual piece. We dont like wild flashy designs. We want our design to be bold and classic while at the same time conveying who we are and what we do. We are reliable, professional, and the best in the business.

Industry/Entity Type

Health Care

Contact Information for Business Card

- Clean
- Bold
- Classic
- not cluttered

Requirements
Must have
• logo, website, phone number
Nice to have
• several options to choose from
Should not have
• flashy imaged - reflective print - images of people sleeping

```html
<!DOCTYPE html>
<html lang="en">
<head>
<meta charset="utf-8">
<title>Steadfast MD – Business Cards</title>
<link href="https://fonts.googleapis.com/css2?family=Archivo:wght@400;500;800&display=swap" rel="stylesheet">
<style>
  :root {
    --bg: #5c5c5c;
    --card-dark: #232323;
    --card-light: #ffffff;
    --red: #e0262b;
    --ink: #111111;
    --ink-soft: #2a2a2a;
    --white: #ffffff;
  }
  * { margin: 0; padding: 0; box-sizing: border-box; }
  html, body { width: 1200px; height: 960px; overflow: hidden; }
  body {
    background: var(--bg);
    font-family: "Archivo", Arial, sans-serif;
    position: relative;
  }
  .card {
    position: absolute;
    left: 230px;
    width: 740px;
    height: 423px;
    overflow: hidden;
    box-shadow: 0 10px 28px rgba(0,0,0,.35);
  }
  .card-front { top: 32px; background: var(--card-dark); }
  .card-back  { top: 505px; background: var(--card-light); }

  /* brand name set as plain text */
  .brand { position: absolute; }
  .brand-name { font-weight: 500; letter-spacing: 1px; white-space: nowrap; }

  .card-front .brand { left: 0; right: 0; top: 140px; text-align: center; }
  .card-front .brand-name { font-size: 58px; color: var(--white); }

  .front-web {
    position: absolute; left: 0; right: 0; top: 280px;
    display: flex; align-items: center; justify-content: center; gap: 16px;
  }
  .front-web .rule { width: 150px; height: 2px; background: var(--red); }
  .front-web .url { font-size: 17px; letter-spacing: 2px; color: var(--white); font-weight: 500; }
  .front-web .url b { color: var(--red); font-weight: 500; }

  .card-back .brand { right: 40px; top: 50px; }
  .card-back .brand-name { font-size: 36px; color: var(--ink); }

  .long-rule {
    position: absolute; left: 250px; right: 40px; top: 150px;
    height: 2px; background: var(--red);
  }
  .address {
    position: absolute; right: 40px; top: 172px;
    text-align: right; font-size: 16px; line-height: 1.35; color: var(--ink-soft);
  }

  .person { position: absolute; left: 50px; top: 205px; }
  .person-name { font-size: 28px; font-weight: 800; color: var(--ink); letter-spacing: 0.5px; }
  .person-name span { color: var(--red); }
  .person-title { font-size: 17px; color: var(--ink-soft); margin-top: 2px; }
  .short-rule { width: 230px; height: 2px; background: var(--red); margin: 10px 0 10px; }

  .contacts { list-style: none; }
  .contacts li {
    display: flex; align-items: center; gap: 10px;
    font-size: 16px; color: var(--ink-soft); line-height: 24px;
  }
  .contacts svg { width: 14px; height: 14px; flex: none; }

  .base-band { position: absolute; left: 0; right: 0; bottom: 0; height: 14px; display: flex; }
  .base-band .red { flex: 0 0 62%; background: var(--red); }
  .base-band .black { flex: 1; background: var(--ink); }
</style>
</head>
<body>

  <section class="card card-front" aria-label="Card front">
    <div class="brand">
      <span class="brand-name">Steadfast MD</span>
    </div>
    <div class="front-web">
      <span class="rule"></span>
      <span class="url">www.<b>steadfastsleep</b>.com</span>
      <span class="rule"></span>
    </div>
  </section>

  <section class="card card-back" aria-label="Card back">
    <div class="brand">
      <span class="brand-name">Steadfast MD</span>
    </div>
    <div class="long-rule"></div>
    <div class="address">Harbor Lane, Suite 12<br>Westfield, 3500, Country</div>

    <div class="person">
      <div class="person-name">DANIEL <span>HART</span></div>
      <div class="person-title">Founder &amp; CEO</div>
      <div class="short-rule"></div>
      <ul class="contacts">
        <li>
          <svg viewBox="0 0 16 16" aria-hidden="true"><path fill="#e0262b" d="M3.5 1.5l2.5 3-1.5 1.5c.8 1.8 2.2 3.2 4 4l1.5-1.5 3 2.5-1.5 2.5C6.5 13.5 2.5 9.5 1 4z"/></svg>
          014 562 8093
        </li>
        <li>
          <svg viewBox="0 0 16 16" aria-hidden="true"><rect x="4" y="1" width="8" height="14" rx="1.5" fill="none" stroke="#e0262b" stroke-width="1.8"/><circle cx="8" cy="12.3" r="0.9" fill="#e0262b"/></svg>
          014 562 8093
        </li>
        <li>
          <svg viewBox="0 0 16 16" aria-hidden="true"><rect x="1" y="3" width="14" height="10" fill="#e0262b"/><path d="M1 3l7 6 7-6" fill="none" stroke="#fff" stroke-width="1.3"/></svg>
          info@steadfastclinic.com
        </li>
        <li>
          <svg viewBox="0 0 16 16" aria-hidden="true"><g fill="none" stroke="#e0262b" stroke-width="1.3"><circle cx="8" cy="8" r="6.5"/><ellipse cx="8" cy="8" rx="3" ry="6.5"/><path d="M1.5 8h13M2.5 4.8h11M2.5 11.2h11"/></g></svg>
          www.steadfastsleep.com
        </li>
      </ul>
    </div>

    <div class="base-band"><span class="red"></span><span class="black"></span></div>
  </section>

</body>
</html>
```